Church Equipping Classes Needing Printed Banner

We are looking for a printed Banner that will be 24x36. I attached and example on the brief. Please visit out website at brenlux.org to see what we do.

Summit Path is the name of our equipping process. It has four classes:

Summit Path - The end goal is to Connect
Harvest Rhythm - Our end goal is for people to get the Culture of the Kingdom
Table of Embers - End goal is they would find Community
Missions - Out-Reachers End goal is they would go on missions.

Our mission is teaching people and reaching nations with the message of Freedom. Galatians 5:1

The concept/idea behind the banner is to communicate this mission as well as the four classes.

Logos to incorporate:
Attached

Please let me know of anything you need to help. We would like our logo on everything but an idea to incorporate the whole concept of Summit Path. Then each class represented as well in that concept. These four classes run each month at our church and each one will have it's on banner and book cover, etc.

The text that the banner should contain is:

Teaching people, Reaching Nations with Freedom.
Galatians 5:1

- Encounter the radical grace & supernatural love of your Heavenly Father!
- Learn something practical and relevant that's guaranteed to work on Sunday AND Monday!
- Connect with others like you- people walking from brokenness into raw grace & unconditional love!
- Discover how you, right now, can change the world!

Target Market(s)

Church members and people outside the church looking for an equipping process.

Industry/Entity Type

Church

Font styles to use
Serif
Sans Serif
Decorative
Script

Colors

Designer to choose colors to be used in the design.

Requirements
Must have
• Logo of our church. Overall concept of Summit Path throughout and each class represented uniquely in the concept. Summit Path is the overall process, but it is also the first class.

```html
<!DOCTYPE html>
<html lang="en">
<head>
<meta charset="utf-8">
<title>Summit Path Equipping Banner</title>
<link href="https://fonts.googleapis.com/css2?family=Source+Sans+3:wght@300;400;600;700&display=swap" rel="stylesheet">
<style>
  :root{
    --page:#0b0b0b;
    --ink:#111111;
    --orange:#e0531d;
    --orange-dark:#c2410f;
    --orange-soft:#f3a86a;
    --white:#ffffff;
    --gold-light:#fff6d8;
  }
  *{box-sizing:border-box;margin:0;padding:0}
  html,body{width:1200px;height:1200px;overflow:hidden;background:var(--page)}
  body{font-family:"Source Sans 3",Arial,sans-serif;color:var(--ink)}
  .banner{position:absolute;left:200px;top:0;width:800px;height:1200px;overflow:hidden}
  .banner__photo{position:absolute;inset:0;
    background:
      radial-gradient(ellipse 70% 35% at 50% 6%, var(--gold-light) 0%, rgba(255,240,200,0) 70%),
      linear-gradient(180deg,#fbe9b4 0%,#f6d889 28%,#e9b45a 52%,#cf8a37 74%,#a9642a 100%);}
  .banner__marker{position:absolute;left:0;top:58px;width:10px;height:50px;background:var(--ink)}
  .tagline{position:absolute;left:32px;top:52px;width:370px;font-size:27px;line-height:33px}
  .tagline__line{font-weight:300;letter-spacing:-0.2px}
  .tagline__ref{font-weight:700}
  .brand{position:absolute;right:36px;top:56px;display:flex;align-items:center;gap:12px}
  .brand__dot{width:28px;height:28px;border-radius:50%;background:var(--ink)}
  .brand__name{font-size:28px;font-weight:600;letter-spacing:0.3px;white-space:nowrap}
  .icon{position:absolute;width:110px;height:115px}
  .icon svg{width:100%;height:100%;fill:none;stroke:var(--ink);stroke-width:5;stroke-linejoin:round;stroke-linecap:round}
  .class-card{position:absolute;width:340px}
  .class-card__title{height:37px;background:linear-gradient(180deg,var(--orange),var(--orange-dark));
    color:var(--ink);font-weight:700;font-size:22px;line-height:37px;padding-left:15px}
  .class-card__body{background:var(--white);height:119px;border-top:3px solid var(--orange-soft);
    padding:12px 15px;font-weight:300;font-size:17.5px;line-height:21.5px}
  .class-card__rule{height:11px;background:var(--ink);margin-top:3px}
</style>
</head>
<body>
<main class="banner">
  <div class="banner__photo" role="img" aria-label="Sunlit wheat field at golden hour with a long-haired girl seen from behind, arms spread wide"></div>
  <div class="banner__marker"></div>

  <header class="tagline">
    <p class="tagline__line">Teaching people, Reaching Nations with Freedom.</p>
    <p class="tagline__ref">Galatians 5:1</p>
  </header>

  <div class="brand">
    <span class="brand__dot"></span>
    <span class="brand__name">Lumen Harbor Outreach</span>
  </div>

  <div class="icon" style="left:155px;top:520px">
    <svg viewBox="0 0 110 115"><path d="M55 4v22M46 12h18M55 26l-22 30v55h44V56z M33 78l-18 12v21h18 M77 78l18 12v21H77 M46 111V94a9 9 0 0 1 18 0v17"/><circle cx="55" cy="60" r="7"/></svg>
  </div>
  <div class="icon" style="left:535px;top:520px">
    <svg viewBox="0 0 110 115"><path d="M18 6h74v90H18z M18 96v8h6 M86 96v8H62l-4 8-4-8H24 M92 6h6v92 M48 26h12v14h14v12H60v32H48V52H34V40h14z"/></svg>
  </div>
  <div class="icon" style="left:155px;top:840px">
    <svg viewBox="0 0 110 115"><circle cx="66" cy="44" r="30"/><circle cx="66" cy="44" r="22"/><path d="M58 36a12 12 0 0 1 16 0 M44 66 20 92a6 6 0 0 0 8 8l26-24z"/></svg>
  </div>
  <div class="icon" style="left:535px;top:840px">
    <svg viewBox="0 0 110 115"><path d="M62 6v10 M30 40c10-20 40-26 56-10s10 36 16 52L12 96c12-10 6-36 18-56z M42 92a14 14 0 0 0 26-6"/></svg>
  </div>

  <section class="class-card" style="left:40px;top:640px">
    <h2 class="class-card__title">Summit Path</h2>
    <p class="class-card__body">Encounter the radical grace &amp; supernatural love of your Heavenly Father!</p>
    <div class="class-card__rule"></div>
  </section>
  <section class="class-card" style="left:420px;top:640px">
    <h2 class="class-card__title">Harvest Rhythm</h2>
    <p class="class-card__body">Learn something practical and relevant that's guaranteed to work on Sunday AND Monday!</p>
    <div class="class-card__rule"></div>
  </section>
  <section class="class-card" style="left:40px;top:960px">
    <h2 class="class-card__title">Table of Embers</h2>
    <p class="class-card__body">Connect with others like you- people walking from brokenness into raw grace &amp; unconditional love!</p>
    <div class="class-card__rule"></div>
  </section>
  <section class="class-card" style="left:420px;top:960px">
    <h2 class="class-card__title">Out-Reachers</h2>
    <p class="class-card__body">Discover how you, right now, can change the world!</p>
    <div class="class-card__rule"></div>
  </section>
</main>
</body>
</html>
```